Marlow Research, Inc. Site Design Project

Marlow Research, Inc is my private and small research office.
This naming shows:
We investigate every(*: asterisk) issue to support society.
We investigate "a star risk" which means every critical things for example, information security, branding, public communication - to understand for our clients - especially innovative person.
Last year, we had faced the great disaster in Japan, we investigated the damaged place, schools, and local governments, and supported communities like Quillfest Ogura.
So I want to get a high concept sites with good logo and to use card, website, and our letter.
Reason: We would like to look for more competitive candidates.
I uploaded the latest logo. If you have any idea to adapt it to your design, I appreciate it.
* marketing section of leading companies(enterprises)
* promotion agencies of government
* futurist and researcher
* business managers
Communication
for desirable future

```html
<!DOCTYPE html>
<html lang="en">
<head>
<meta charset="utf-8">
<title>Marlow Research</title>
<link rel="stylesheet" href="https://fonts.googleapis.com/css2?family=Cinzel:wght@400;700&family=Arimo:wght@400;700&display=swap">
<style>
:root{
  --orange:#f5810f;
  --heading:#f28a12;
  --red:#e8261a;
  --slate:#2e3a44;
  --text:#444;
  --dark:#222;
  --frame:#c9c1c4;
  --white:#fff;
}
*{margin:0;padding:0;box-sizing:border-box}
html,body{width:975px;height:1200px;overflow:hidden;background:var(--white)}
.page{position:absolute;left:0;top:0;width:960px;height:1181px;transform:scale(1.0156,1.0161);transform-origin:0 0;font-family:"Arimo",Arial,sans-serif;color:var(--text)}
.abs{position:absolute}
.hero-photo{left:0;top:0;width:400px;height:467px;background:linear-gradient(160deg,#dfe3e2 0%,#f3f4f2 35%,#e9ecec 60%,#cfd6d6 100%)}
.brand-mark{left:8px;top:8px;font-family:"Cinzel",serif;font-size:14px;color:var(--red)}
.top-band{left:400px;top:0;width:560px;height:78px;background:var(--orange)}
.top-nav{right:16px;top:24px;font-size:12px;color:var(--white)}
.top-nav span{margin:0 14px}
.menu-card{left:353px;top:52px;width:354px;height:349px;background:var(--white);border:1px solid #c8c8c8}
.menu-panel{left:15px;top:14px;width:321px;height:321px;background:var(--slate)}
.menu-title{left:31px;top:24px;font-family:"Arimo",Arial,sans-serif;font-weight:700;font-size:25px;color:var(--red);letter-spacing:-.3px}
.menu-list{list-style:none;left:54px;top:68px}
.menu-list li{height:48px;display:flex;align-items:center;font-family:"Cinzel",serif;font-size:18px;color:var(--white);letter-spacing:1px;text-transform:uppercase}
.menu-list svg{width:20px;height:22px;margin-right:34px}
.section-title{font-family:"Cinzel",serif;color:var(--heading);font-weight:400;white-space:nowrap}
.body-copy{font-size:11px;line-height:20px}
.body-copy span{display:block;text-align:justify;text-align-last:justify;white-space:nowrap}
.body-copy span.end{text-align-last:left}
.wide-copy{line-height:24px}
.read-more{font-size:12px;font-weight:700;color:var(--dark)}
.news-date{font-size:14px;font-weight:700;color:var(--dark)}
.gallery-frame{left:21px;top:892px;width:380px;height:220px;background:var(--frame)}
.gallery-image{left:8px;top:8px;width:364px;height:204px;background:linear-gradient(135deg,#c8d8ea 0%,#3f6fa8 35%,#12305a 60%,#0a0f18 100%)}
.contact-lines{left:441px;top:896px;font-family:"Cinzel",serif;font-size:15px;line-height:20px;color:#333;letter-spacing:.5px}
.footer-fade{left:0;top:1088px;width:960px;height:38px;background:#f7fafa}
.site-footer{left:0;top:1126px;width:960px;height:55px;background:var(--slate)}
.site-footer p{position:absolute;left:22px;top:14px;font-family:"Cinzel",serif;font-size:13px;color:var(--white)}
</style>
</head>
<body>
<div class="page">
  <div class="abs hero-photo" role="img" aria-label="Photo of three smiling researchers in white lab coats inside a bright greenhouse"></div>
  <div class="abs brand-mark">Marlow Research</div>

  <div class="abs top-band"></div>
  <nav class="abs top-nav">Home Page<span>|</span>Contact Us</nav>

  <div class="abs menu-card">
    <div class="abs menu-panel">
      <div class="abs menu-title">MARLOW RESEARCH</div>
      <ul class="abs menu-list">
        <li><svg viewBox="0 0 20 22"><path d="M2 1 L18 11 L2 21 L8 11 Z" fill="var(--red)"/></svg>About Us</li>
        <li><svg viewBox="0 0 20 22"><path d="M2 1 L18 11 L2 21 L8 11 Z" fill="var(--red)"/></svg>Services</li>
        <li><svg viewBox="0 0 20 22"><path d="M2 1 L18 11 L2 21 L8 11 Z" fill="var(--red)"/></svg>Products</li>
        <li><svg viewBox="0 0 20 22"><path d="M2 1 L18 11 L2 21 L8 11 Z" fill="var(--red)"/></svg>Enquiry</li>
        <li><svg viewBox="0 0 20 22"><path d="M2 1 L18 11 L2 21 L8 11 Z" fill="var(--red)"/></svg>Contact Us</li>
      </ul>
    </div>
  </div>

  <h2 class="abs section-title" style="left:730px;top:104px;font-size:19px">What We Do</h2>
  <p class="abs body-copy" style="left:729px;top:144px;width:215px">
    <span>Lorem Ipsum is simply dummy text of the</span>
    <span>printing and typesetting industry. Lorem</span>
    <span>Ipsum has been the industry's standard</span>
    <span>dummy text ever since the 1500s, when</span>
    <span>an unknown printer took a galley of type</span>
    <span>and scrambled it to make a type</span>
    <span>specimen book. It has survived not only</span>
    <span class="end">five centuries,</span>
  </p>
  <p class="abs body-copy" style="left:729px;top:324px;width:215px">
    <span>Lorem Ipsum is simply dummy text of the</span>
    <span>printing and typesetting industry. Lorem</span>
    <span>Ipsum has been the industry's standard</span>
    <span>dummy text ever since the 1500s, when</span>
  </p>
  <p class="abs body-copy" style="left:415px;top:403px;width:529px">
    <span>Lorem Ipsum is simply dummy text of the printing and typesetting industry. Lorem Ipsum has been</span>
    <span>the industry's standard dummy text ever since the 1500s, when an unknown printer took a galley of</span>
  </p>
  <div class="abs read-more" style="right:15px;top:456px">READ MORE...</div>

  <h2 class="abs section-title" style="left:8px;top:486px;font-size:25px">Welcome to Marlow Research</h2>
  <p class="abs body-copy wide-copy" style="left:12px;top:530px;width:678px">
    <span>Lorem Ipsum is simply dummy text of the printing and typesetting industry. Lorem Ipsum has been the industry's standard dummy</span>
    <span>text ever since the 1500s, when an unknown printer took a galley of type and scrambled it to make a type specimen book. It has</span>
    <span>survived not only five centuries, but also the leap into electronic typesetting, remaining essentially unchanged. It was popularised</span>
    <span>in the 1960s with the release of Letraset sheets containing Lorem Ipsum passages, and more recently with desktop publishing</span>
    <span class="end">software like Aldus PageMaker including versions of Lorem Ipsum.</span>
  </p>
  <p class="abs body-copy wide-copy" style="left:12px;top:674px;width:678px">
    <span>Lorem Ipsum is simply dummy text of the printing and typesetting industry. Lorem Ipsum has been the industry's standard dummy</span>
    <span>text ever since the 1500s, when an unknown printer took a galley of type and scrambled it to make a type specimen book. It has</span>
    <span>survived not only five centuries, but also the leap into electronic typesetting, remaining essentially unchanged. It was popularised</span>
    <span>in the 1960s with the release of Letraset sheets containing Lorem Ipsum passages, and more recently with desktop publishing</span>
    <span class="end">software like Aldus PageMaker including versions of Lorem Ipsum.</span>
  </p>
  <div class="abs read-more" style="right:272px;top:801px">READ MORE...</div>

  <h2 class="abs section-title" style="left:731px;top:486px;font-size:26px">Latest News</h2>
  <div class="abs news-date" style="left:732px;top:551px">June 20th, 2012</div>
  <p class="abs body-copy" style="left:732px;top:590px;width:203px">
    <span>Amet, consectetuer adipis cing elit sed</span>
    <span>diam nonummy nibh erat volutpat. Ut</span>
    <span>wisi enim ad minim veniamuis nostrud</span>
    <span class="end">exerci tation ullamc orper.</span>
  </p>
  <div class="abs read-more" style="right:28px;top:693px">READ MORE...</div>
  <div class="abs news-date" style="left:732px;top:731px">June 20th, 2012</div>
  <p class="abs body-copy" style="left:732px;top:770px;width:203px">
    <span>Amet, consectetuer adipis cing elit sed</span>
    <span>diam nonummy nibh erat volutpat. Ut</span>
    <span>wisi enim ad minim veniamuis nostrud</span>
    <span class="end">exerci tation ullamc orper.</span>
  </p>
  <div class="abs read-more" style="right:28px;top:873px">READ MORE...</div>
  <div class="abs news-date" style="left:732px;top:911px">June 20th, 2012</div>
  <p class="abs body-copy" style="left:732px;top:950px;width:203px">
    <span>Amet, consectetuer adipis cing elit sed</span>
    <span>diam nonummy nibh erat volutpat. Ut</span>
    <span>wisi enim ad minim veniamuis nostrud</span>
    <span class="end">exerci tation ullamc orper.</span>
  </p>
  <div class="abs read-more" style="right:28px;top:1053px">READ MORE...</div>

  <h2 class="abs section-title" style="left:23px;top:847px;font-size:22px">Gallery</h2>
  <div class="abs gallery-frame">
    <div class="abs gallery-image" role="img" aria-label="Image of a satellite orbiting above the blue curve of the Earth"></div>
  </div>

  <h2 class="abs section-title" style="left:436px;top:850px;font-size:21px">Contact Us</h2>
  <div class="abs contact-lines">
    <p>MARLOW RESEARCH LTD.</p>
    <p>ABC -66, CITY</p>
    <p>&nbsp;</p>
    <p>Phone-91-000-00-0000</p>
    <p>Toll free-0000-000-000</p>
  </div>

  <div class="abs footer-fade"></div>
  <footer class="abs site-footer"><p>Copyright © 2012 . All Rights Reserved.</p></footer>
</div>
</body>
</html>
```